Craft beer central! New brew pub needs website that doesn't suck.

We are a new brewpub in Picton, Ontario. We have a kitchen and are about to start with our own beer. Currently I have a really horrid horrid website.

Check it out www.thehollowlarder.example (please don't laugh too hard)

I'm on Facebook as well which might give a better idea of who we are
(it's my main social media)
https://www.facebook.com/millstreamslarder

(there is a long story with the name difference)

I want something that I can edit myself (things like events, dates,etc), change the menu pdf, add events, have a contact page, have a gallery of pics, our beer/wine menu and eventually what we are putting on tap ourselves.

We currently have 16 craft beers on tap, local wine and our tag line is "explore the bounty of the county".
Updates

Project Deadline Extended
Reason: Sorry to have extended it. Have a few things on this week. Cheers,

Target Market(s)

craft beer, tourists.

Industry/Entity Type

Hospitality

Number of Pages Required

4 page

Font styles to use
Other font styles liked:
• Museo slab and next bold.

Requirements
Must have
• Must be able to attach a menu pdf (I have a food menu and beer/wine menu)
• Must have an events page so I can edit/ add them as we go on
• contacts page
• Must have a gallery that I can edit/swap pictures.
Nice to have
• Modern, hip looking page. Love black, white, grey and a splash of red.
Should not have
• be a feminine looking site. look at our Facebook page to look at our decor.

```html
<!DOCTYPE html>
<html lang="en">
<head>
<meta charset="utf-8">
<title>Hollow Larder</title>
<link href="https://fonts.googleapis.com/css2?family=Open+Sans:ital,wght@0,300;0,400;0,600;0,700;1,400;1,600&family=Roboto+Slab:wght@300;700&display=swap" rel="stylesheet">
<style>
:root{
  --red:#e31e24;
  --red-dark:#c5161c;
  --ink:#1d1d1d;
  --charcoal:#2a2a2a;
  --grey:#ebebeb;
  --mid:#6d6d6d;
  --white:#ffffff;
}
*{box-sizing:border-box;margin:0;padding:0}
html,body{width:813px;height:1200px;overflow:hidden}
body{font-family:"Open Sans",Arial,sans-serif;color:var(--ink);background:var(--white);position:relative}

/* hero */
.hero{position:absolute;left:0;top:0;width:813px;height:303px;
  background:radial-gradient(ellipse at 70% 35%,#8a7a6a 0%,#4a3f36 35%,#1e1a17 75%);}
.brand{position:absolute;left:322px;top:0;width:170px;height:74px;background:var(--white);
  border-radius:0 0 14px 14px;display:flex;align-items:center;justify-content:center;gap:8px;
  font-family:"Roboto Slab",serif;font-weight:700;font-size:17px;color:var(--ink);letter-spacing:.5px}
.brand .dot{width:12px;height:12px;background:var(--red);border-radius:50%}
.nav{position:absolute;top:82px;left:280px;display:flex;gap:18px;font-size:11px;font-weight:600;color:var(--white)}
.nav .active{color:var(--red)}
.badge{position:absolute;left:386px;top:122px;width:42px;height:42px;border-radius:50%;background:var(--red);
  display:flex;align-items:center;justify-content:center}
.tagline{position:absolute;top:215px;width:100%;text-align:center;color:var(--white);
  font-style:italic;font-weight:600;font-size:22px}
.slide-arrow{position:absolute;top:140px;width:18px;height:22px;background:var(--red);display:flex;align-items:center;justify-content:center}
.slide-arrow.left{left:0}.slide-arrow.right{right:0}

/* category tiles */
.tiles{position:absolute;top:303px;left:0;width:813px;height:97px;display:flex}
.tile{flex:1;display:flex;align-items:center;justify-content:center;color:var(--white);
  font-size:20px;font-weight:700}
.tile.menu{background:#1c1c1c}
.tile.breakfast{background:linear-gradient(135deg,#5b4a3c,#2c241e)}
.tile.lunch{background:linear-gradient(135deg,#6a5540,#30261d)}
.tile.dinner{background:linear-gradient(135deg,#4e3f35,#231c17)}

/* welcome */
.welcome{position:absolute;top:400px;left:0;width:813px;height:155px;text-align:center}
.section-title{font-family:"Roboto Slab",serif;font-weight:700;color:var(--red);font-size:22px;letter-spacing:.5px}
.welcome .section-title{margin-top:18px}
.welcome p{width:520px;margin:14px auto 0;font-size:8.5px;line-height:1.5;color:var(--mid)}
.btn{display:inline-block;background:var(--red);color:var(--white);font-size:9px;font-weight:700;
  padding:6px 12px;margin-top:12px}

/* events */
.events{position:absolute;top:555px;left:0;width:813px;height:245px;background:var(--grey);text-align:center}
.events .section-title{margin-top:10px}
.event-row{position:absolute;top:42px;left:114px;display:flex;gap:15px}
.event{width:130px;height:183px;position:relative;color:var(--white);text-align:center;
  background:linear-gradient(180deg,#4a4038,#1f1b18)}
.event.featured{background:var(--red)}
.event h3{font-size:11px;font-weight:700;margin-top:8px}
.event .teaser{font-size:7px;line-height:1.4;padding:6px 10px;opacity:.9}
.event .day{position:absolute;top:108px;width:100%;font-size:26px;font-weight:300;opacity:.55}
.event .year{position:absolute;top:142px;width:100%;font-size:26px;font-weight:700}
.ev-arrow{position:absolute;top:128px;width:14px;height:18px;background:var(--charcoal);display:flex;align-items:center;justify-content:center}
.ev-arrow.left{left:88px}.ev-arrow.right{left:711px}

/* newsletter */
.newsletter{position:absolute;top:800px;left:0;width:813px;height:135px;
  background:linear-gradient(180deg,#262220,#141210);text-align:center;color:var(--white)}
.newsletter h2{font-weight:400;font-size:19px;margin-top:32px}
.signup{display:flex;justify-content:center;gap:22px;margin-top:18px}
.signup .field{width:245px;height:26px;background:#5a5a5a;color:#cfcfcf;font-size:9px;text-align:left;padding:7px 10px}
.signup .submit{width:110px;height:26px;background:var(--red);font-size:10px;padding-top:6px}

/* gallery */
.gallery{position:absolute;top:935px;left:0;width:813px;height:175px;background:var(--grey);text-align:center}
.gallery .section-title{margin-top:8px}
.thumbs{position:absolute;top:32px;left:114px;display:flex;gap:30px}
.thumb{width:110px;height:105px;background:linear-gradient(135deg,#6b5a4c,#2e2621)}
.thumb.b{background:linear-gradient(135deg,#8a7260,#3b302a)}
.thumb.c{background:linear-gradient(135deg,#5d5450,#242020)}
.thumb.d{background:linear-gradient(135deg,#7a6455,#342a24)}
.gal-arrow{position:absolute;top:72px;width:14px;height:18px;background:var(--red);display:flex;align-items:center;justify-content:center}
.gal-arrow.left{left:88px}.gal-arrow.right{left:711px}

/* footer */
.footer{position:absolute;top:1110px;left:0;width:813px;height:90px;background:var(--red);color:var(--white);text-align:center}
.footer-nav{display:flex;justify-content:center;gap:28px;font-size:9px;margin-top:20px}
.social{display:flex;justify-content:center;gap:5px;margin-top:10px}
.social span{width:13px;height:13px;background:var(--red-dark);border:1px solid rgba(255,255,255,.6)}
.copy{font-size:7px;margin-top:8px;opacity:.9}
.to-top{position:absolute;right:20px;top:40px;font-size:8px}
</style>
</head>
<body>

<header class="hero" role="img" aria-label="Photo of wine glasses on a set restaurant table">
  <div class="brand"><span class="dot"></span>Hollow Larder</div>
  <nav class="nav"><span class="active">Home</span><span>Menu</span><span>Events</span><span>Gallery</span><span>Contact us</span></nav>
  <div class="badge"><svg width="20" height="20" viewBox="0 0 20 20"><polygon points="10,1 12.5,7 19,7.5 14,11.8 15.6,18.5 10,15 4.4,18.5 6,11.8 1,7.5 7.5,7" fill="#fff"/></svg></div>
  <p class="tagline">"Explore the bounty of the county"</p>
  <div class="slide-arrow left"><svg width="6" height="8"><polygon points="6,0 0,4 6,8" fill="#fff"/></svg></div>
  <div class="slide-arrow right"><svg width="6" height="8"><polygon points="0,0 6,4 0,8" fill="#fff"/></svg></div>
</header>

<section class="tiles">
  <div class="tile menu">Menu</div>
  <div class="tile breakfast" role="img" aria-label="Breakfast plate photo">Breakfast</div>
  <div class="tile lunch" role="img" aria-label="Lunch dish photo">Lunch</div>
  <div class="tile dinner" role="img" aria-label="Dinner dish photo">Dinner</div>
</section>

<section class="welcome">
  <h1 class="section-title">WELCOME TO HOLLOW LARDER</h1>
  <p>The Hollow Larder is a celebration of the bounty of the county. Sixteen local craft beers on tap, wine from nearby vineyards and a kitchen built on seasonal produce. Pull up a stool, meet your neighbours and stay for another round with us.</p>
  <span class="btn">READ MORE</span>
</section>

<section class="events">
  <h2 class="section-title">EVENTS</h2>
  <div class="ev-arrow left"><svg width="5" height="8"><polygon points="5,0 0,4 5,8" fill="#fff"/></svg></div>
  <div class="event-row">
    <article class="event" role="img" aria-label="Event photo"><h3>SUSCIPIANTUR</h3><div class="day">10/07</div><div class="year">2015</div></article>
    <article class="event featured"><h3>VITUPERATA</h3><p class="teaser">Live music on the patio with a new seasonal ale on tap all night long.</p><div class="day">12/07</div><div class="year">2015</div></article>
    <article class="event" role="img" aria-label="Event photo"><h3>DESCIPIANTUR</h3><div class="day">15/07</div><div class="year">2015</div></article>
    <article class="event" role="img" aria-label="Event photo"><h3>GEORGAANTUR</h3><div class="day">17/07</div><div class="year">2015</div></article>
  </div>
  <div class="ev-arrow right"><svg width="5" height="8"><polygon points="0,0 5,4 0,8" fill="#fff"/></svg></div>
</section>

<section class="newsletter" role="img" aria-label="Dimmed restaurant interior photo behind signup">
  <h2>Get our daily food items delivered to your E-mail</h2>
  <div class="signup"><div class="field">Your Email ID</div><div class="submit">Subscribe</div></div>
</section>

<section class="gallery">
  <h2 class="section-title">GALLERY</h2>
  <div class="gal-arrow left"><svg width="5" height="8"><polygon points="5,0 0,4 5,8" fill="#fff"/></svg></div>
  <div class="thumbs">
    <div class="thumb" role="img" aria-label="Bar shelf photo"></div>
    <div class="thumb b" role="img" aria-label="Plated food photo"></div>
    <div class="thumb c" role="img" aria-label="Dining room photo"></div>
    <div class="thumb d" role="img" aria-label="Kitchen team photo"></div>
  </div>
  <div class="gal-arrow right"><svg width="5" height="8"><polygon points="0,0 5,4 0,8" fill="#fff"/></svg></div>
</section>

<footer class="footer">
  <nav class="footer-nav"><span>Home</span><span>About Us</span><span>What We Do</span><span>Who We Are</span><span>Tools</span><span>Contact us</span></nav>
  <div class="social"><span></span><span></span><span></span><span></span></div>
  <p class="copy">Copyright 2015. All Rights Reserved</p>
  <span class="to-top">▲</span>
</footer>

</body>
</html>
```